New therapy private practice needs a 2 sided postcard announcing location and services

We need a postcard sized card that is TWO SIDED and shares our new location and services offered. (new location is 3840. W. 58th #2200 in Tulsa, OK 74129) Name of the therapy business is "Calm Harbor Counseling". Services offered include individual, marriage, family and group counseling. My phone number to place on the card is (918) 555-0148 and someone can call to schedule a free 20 minute consultation at that number.

These cards will also be mailed in an enclosed envelope or placed in welcome baskets as a marketing tool with possible referral sources like churches, doctors, and lawyers. (That means there does not have to be a space for an address or stamp to mail to. Full use of both sides of the card is important) We would like to see designs that use softer colors such as blue, purples, or greens. The final design should communicate a feeling of peace and hope and a sense of freshness and approachability. Incorporating a tag line such as..... "where you'll find hope!" would be good. My website is www.calmharborcare.example and extra info about my practice is on there. It is important my credentials are listed on the postcard. Dana Ruth Pell, LPC-S, LMFT

I am not looking for a bunch of "box looking pictures". The pictures I am uploading are for ideas, although my logo and picture should be used. I like the type of picture I have on my homepage of my website with the quote "Let your hopes, not your fears shape your future"

Target Market(s)

Primarily women and couples looking for counseling for relationships, anxiety, depression, or life transitions.

Font styles to use
Serif
Script

Colors
3276b5
85acd3
86cfc6
33b8a4
cadf82
876aae
9bcb3c

Requirements
Must have
• My picture, address, website, and phone number as well as my logo.
• Address is: 3840 W. 58th Street #2200 Tulsa, OK 74129
• Web: www.calmharborcare.example
• Email: dana@calmharborcare.example
• Phone: (918) 555-0148
• "Hope anchors the soul" - Heb. 6:19
• On my website, I have a 2 minute video of myself. This may be helpful to watch in getting a "feel" for my counseling practice.
• Services Provided: ANXIETY | DEPRESSION | LIFE TRANSITIONS | MARRIAGE COUNSELING | SEPARATION AND DIVORCE | WOMEN’S ISSUES | ADDICTIONS AND INFIDELITY | PARENT/CHILD RELATIONSHIPS | FAMILY CONFLICT | TRAUMA/GRIEF AND LOSS
Nice to have
• A combination of print and script would be nice. A feeling of tranquility and hope
• I would like to have the statement at the bottom of the card.... " It is my desire for you to discover that no matter the situation you are currently going through….. there’s hope!"
• It would also be nice to have a small area that says: Dana is a graduate of Western Lakeview College and has been in private practice for 11 years. She is a regular monthly co-host on the Meadow Broadcast Group at 88.3 FM
Should not have
• Heavy bold or abrasive feel

```html
<!DOCTYPE html>
<html lang="en">
<head>
<meta charset="utf-8">
<title>Calm Harbor Counseling – Postcard</title>
<link rel="stylesheet" href="https://fonts.googleapis.com/css2?family=Montserrat:wght@400;500;600;700;800&family=Cormorant+Garamond:ital,wght@1,500;1,600&display=swap">
<style>
  :root{
    --stage:#2f5a28;
    --brand-green:#467d39;
    --ink:#111111;
    --paper:#ffffff;
    --text-dark:#1e1e1e;
    --forest-gold:#d8b44c;
    --forest-rust:#b4683e;
    --forest-haze:#cfd2a0;
    --forest-plum:#a3588f;
    --forest-rose:#d2679c;
  }
  *{box-sizing:border-box;margin:0;padding:0}
  html,body{width:1200px;height:1200px;overflow:hidden}
  body{background:radial-gradient(circle at 50% 50%,#467a38 0,#2f5a28 55%,#22441d 100%);font-family:"Montserrat",sans-serif;position:relative}
  .card{position:absolute;overflow:hidden;background:var(--paper)}
  .card svg.shapes{position:absolute;inset:0;width:100%;height:100%}
  .card-front{left:70px;top:83px;width:702px;height:507px}
  .card-back{left:421px;top:622px;width:698px;height:506px}

  /* front */
  .forest-photo{position:absolute;inset:0;
    background:
      radial-gradient(ellipse 170px 230px at 300px 250px,#e9cf8e 0,rgba(233,207,142,0) 100%),
      radial-gradient(ellipse 200px 160px at 170px 300px,#e8d65a 0,rgba(232,214,90,0) 100%),
      radial-gradient(ellipse 190px 170px at 600px 60px,var(--forest-rose) 0,rgba(210,103,156,0) 100%),
      radial-gradient(ellipse 160px 170px at 520px 280px,#c7a3d6 0,rgba(199,163,214,0) 100%),
      radial-gradient(ellipse 260px 120px at 140px 470px,#c0502c 0,rgba(192,80,44,0) 100%),
      radial-gradient(ellipse 220px 110px at 620px 380px,var(--forest-rust) 0,rgba(180,104,62,0) 100%),
      linear-gradient(135deg,var(--forest-haze) 0,var(--forest-gold) 40%,var(--forest-rust) 70%,var(--forest-plum) 100%)}
  .logo-box{position:absolute;left:427px;top:55px;width:275px;height:117px;background:var(--paper);
    display:flex;align-items:center;justify-content:center;gap:10px}
  .logo-dot{width:16px;height:16px;border-radius:50%;background:var(--brand-green)}
  .logo-name{font-weight:700;font-size:19px;color:var(--brand-green);line-height:1.15}
  .verse{position:absolute;left:440px;top:200px;width:245px;text-align:center;color:var(--paper)}
  .verse-text{font-family:"Cormorant Garamond",serif;font-style:italic;font-weight:600;font-size:27px;line-height:1.1}
  .verse-ref{font-size:12px;font-weight:600;letter-spacing:1.5px;margin-top:6px}
  .tagline{position:absolute;left:0;width:100%;top:381px;text-align:center;font-weight:700;
    font-size:28px;line-height:32px;color:var(--brand-green)}
  .tagline-sub{position:absolute;left:0;width:100%;top:414px;text-align:center;font-size:12.5px;color:var(--text-dark)}

  /* back */
  .services{position:absolute;left:0;width:100%;top:51px;text-align:center;font-size:15.6px;
    line-height:22.5px;color:var(--text-dark)}
  .services .dot{color:var(--brand-green);font-weight:700;margin:0 4px}
  .cta-lead{position:absolute;left:0;width:698px;top:187px;text-align:center;font-weight:600;font-size:19px;color:var(--paper)}
  .cta-pill{position:absolute;left:163px;top:214px;width:373px;height:28px;border-radius:14px;background:var(--paper);
    text-align:center;font-weight:800;font-size:17.5px;line-height:28px;color:var(--brand-green)}
  .counselor-name{position:absolute;left:272px;top:276px;font-weight:700;font-size:24px;color:var(--brand-green)}
  .counselor-cred{position:absolute;left:255px;top:305px;font-size:21px;color:var(--paper)}
  .contact{position:absolute;color:var(--paper);font-size:13.5px;display:flex;align-items:flex-start;gap:6px;line-height:18px}
  .contact svg{flex:none;margin-top:2px}
  .contact-phone{font-weight:700;font-size:14.5px}
  .portrait{position:absolute;left:506px;top:314px;width:180px;height:192px;border-radius:90px 90px 0 0;
    background:radial-gradient(circle at 50% 35%,#d9b98a 0,#b08a63 35%,#6d2b45 70%,#3a1a2a 100%)}
</style>
</head>
<body>

<section class="card card-front" aria-label="Postcard front">
  <div class="forest-photo" role="img" aria-label="Photo of a woman praying in a glowing autumn forest"></div>
  <svg class="shapes" viewBox="0 0 702 507" preserveAspectRatio="none">
    <polygon points="0,0 130,0 102,61" fill="var(--paper)"/>
    <polygon points="0,0 102,61 0,269" fill="var(--brand-green)"/>
    <polygon points="130,0 268,0 0,292 0,269 102,61" fill="var(--ink)"/>
    <polygon points="560,377 702,313 702,377" fill="var(--paper)"/>
    <rect x="0" y="377" width="702" height="57" fill="var(--paper)"/>
    <polygon points="430,507 560,434 702,434 702,418 480,507" fill="var(--paper)"/>
    <polygon points="480,507 702,418 702,507" fill="var(--brand-green)"/>
  </svg>
  <div class="logo-box">
    <span class="logo-dot"></span>
    <span class="logo-name">Calm Harbor<br>Counseling</span>
  </div>
  <div class="verse">
    <p class="verse-text">“Hope anchors the soul”</p>
    <p class="verse-ref">HEB. 6:19</p>
  </div>
  <p class="tagline">"WHERE YOU'LL FIND HOPE!"</p>
  <p class="tagline-sub">Dana can be heard monthly on the Meadow Broadcast Group at 88.3 FM</p>
</section>

<section class="card card-back" aria-label="Postcard back">
  <svg class="shapes" viewBox="0 0 698 506" preserveAspectRatio="none">
    <defs>
      <linearGradient id="valleyDusk" x1="0" y1="0" x2="0" y2="1">
        <stop offset="0" stop-color="#5a5a52"/>
        <stop offset=".5" stop-color="#3b3a2e"/>
        <stop offset="1" stop-color="#2a2420"/>
      </linearGradient>
    </defs>
    <rect x="114" y="0" width="470" height="23" fill="var(--brand-green)"/>
    <polygon points="0,172 260,290 200,506 0,506" fill="url(#valleyDusk)" role="img" aria-label="Photo of a person sitting on a rock overlooking a forested valley"/>
    <polygon points="180,200 434,142 515,118 698,342 698,506 200,506 255,300" fill="var(--ink)"/>
    <polygon points="0,162 171,125 698,172 123,296 0,172" fill="var(--brand-green)"/>
  </svg>

  <p class="services">
    <span class="dot">•</span>ANXIETY <span class="dot">•</span>DEPRESSION <span class="dot">•</span>LIFE TRANSITIONS <span class="dot">•</span>MARRIAGE COUNSELING<br>
    <span class="dot">•</span>SEPARATION AND DIVORCE <span class="dot">•</span>WOMEN’S ISSUES <span class="dot">•</span>ADDICTIONS AND INFIDELITY<br>
    <span class="dot">•</span>PARENT/CHILD RELATIONSHIPS <span class="dot">•</span>FAMILY CONFLICT <span class="dot">•</span>TRAUMA/GRIEF AND LOSS
  </p>

  <p class="cta-lead">CALL TO SCHEDULE A</p>
  <p class="cta-pill">FREE 20 MINUTE CONSULTATION</p>

  <p class="counselor-name">DANA RUTH</p>
  <p class="counselor-cred">PELL, LPC-S, LMFT</p>

  <div class="contact" style="left:276px;top:363px">
    <svg width="11" height="15" viewBox="0 0 11 15"><path d="M5.5 0A5.5 5.5 0 0 0 0 5.5C0 9.5 5.5 15 5.5 15S11 9.5 11 5.5A5.5 5.5 0 0 0 5.5 0Zm0 7.6a2.1 2.1 0 1 1 0-4.2 2.1 2.1 0 0 1 0 4.2Z" fill="var(--brand-green)"/></svg>
    <span>3840 W. 58th Street<br>#2200 Tulsa, OK 74129</span>
  </div>
  <div class="contact contact-phone" style="left:296px;top:411px">
    <svg width="13" height="15" viewBox="0 0 13 15"><path d="M3 0 5 4 3.5 5.5C4.3 7.8 5.6 9.6 7.5 11L9 9.5l4 2.2L11.5 15C5 14 0.5 8 0 1.5Z" fill="var(--brand-green)"/></svg>
    <span>918.555.0148</span>
  </div>
  <div class="contact" style="left:254px;top:432px">
    <svg width="15" height="11" viewBox="0 0 15 11"><rect width="15" height="11" fill="var(--brand-green)"/><path d="M0 0 7.5 6 15 0" stroke="var(--ink)" stroke-width="1.3" fill="none"/></svg>
    <span>dana@calmharborcare.example</span>
  </div>
  <div class="contact" style="left:254px;top:453px">
    <svg width="14" height="14" viewBox="0 0 14 14"><circle cx="7" cy="7" r="6" fill="none" stroke="var(--brand-green)" stroke-width="1.4"/><path d="M1 7h12M7 1c-3 3-3 9 0 12M7 1c3 3 3 9 0 12" stroke="var(--brand-green)" stroke-width="1.1" fill="none"/></svg>
    <span>www.calmharborcare.example</span>
  </div>

  <div class="portrait" role="img" aria-label="Portrait photo of counselor Dana Ruth Pell"></div>
</section>

</body>
</html>
```